Brinehaven 52 Sailing Magazine

I need a magazine layout for a new sailing magazine (called 'Brinehaven 52'). I would like to see designs for both the cover as well as the inside spread and the template should allow for content to be dropped into it. Please note that on an ongoing basis, I would prefer to provide the content to the designer, who then adds it to the template, making the necessary edits).

Colors

Designer to choose colors to be used in the design.

Requirements
Must have
• Classy modern design, nautical colors and theme (but clean and modern)
Should not have
• Tacky, old school sailing stuff. Also, here is a great example of how I don't want it to look! Like so many other magazines, the ads take over and give the magazine a very unsophisticated feel. Click on the magazine at this website to see it's inside pages:
• https://www.corvalquay-mag.example/

```html
<!DOCTYPE html>
<html lang="en">
<head>
<meta charset="utf-8">
<title>Brinehaven 52 — Cover</title>
<link rel="stylesheet" href="https://fonts.googleapis.com/css2?family=Archivo:wght@700;800&family=Archivo+Narrow:wght@700&family=Montserrat:wght@500&family=Raleway:wght@300&display=swap">
<style>
  :root {
    --sky-top: #c23a10;
    --sky-mid: #e2641f;
    --sky-glow: #f2a44e;
    --sun-haze: rgba(255, 214, 150, 0.75);
    --horizon: #c9a27c;
    --hull-shadow: rgba(24, 38, 48, 0.55);
    --water-light: #3f8f95;
    --water-deep: #17474e;
    --brand-yellow: #f4ee2a;
    --white: #ffffff;
    --ink-soft: rgba(255, 255, 255, 0.92);
    --page-bg: #e3e3e3;
  }
  * { margin: 0; padding: 0; box-sizing: border-box; }
  html, body {
    width: 1127px;
    height: 1200px;
    overflow: hidden;
    background: var(--page-bg);
  }
  .cover {
    position: relative;
    width: 1127px;
    height: 1200px;
    overflow: hidden;
  }
  .cover-photo {
    position: absolute;
    inset: 0;
    background:
      radial-gradient(ellipse 55% 22% at 38% 50%, var(--sun-haze) 0%, rgba(255, 214, 150, 0) 100%),
      radial-gradient(ellipse 70% 14% at 35% 64%, var(--hull-shadow) 0%, rgba(24, 38, 48, 0) 100%),
      linear-gradient(180deg,
        var(--sky-top) 0%,
        var(--sky-mid) 20%,
        var(--sky-glow) 38%,
        var(--horizon) 52%,
        var(--water-light) 66%,
        var(--water-deep) 100%);
  }
  .masthead {
    position: absolute;
    left: 70px;
    top: 110px;
    width: 860px;
  }
  .tagline {
    font-family: "Archivo", Arial, sans-serif;
    font-weight: 800;
    font-size: 24px;
    color: var(--white);
    text-align: right;
    padding-right: 20px;
    margin-bottom: 6px;
  }
  .brand-name {
    font-family: "Archivo", Arial, sans-serif;
    font-weight: 800;
    font-size: 128px;
    line-height: 1;
    color: var(--brand-yellow);
    letter-spacing: -2px;
    white-space: nowrap;
  }
  .issue-line {
    font-family: "Montserrat", Arial, sans-serif;
    font-weight: 500;
    font-size: 20px;
    letter-spacing: 1px;
    color: var(--ink-soft);
    margin-top: 12px;
    margin-left: 150px;
  }
  .cover-lines {
    position: absolute;
    left: 470px;
    top: 730px;
    width: 630px;
  }
  .lead-story {
    font-family: "Raleway", Arial, sans-serif;
    font-weight: 300;
    font-size: 70px;
    line-height: 0.95;
    color: var(--white);
    letter-spacing: 1px;
    text-transform: uppercase;
    margin-bottom: 16px;
  }
  .teasers { list-style: none; }
  .teasers li {
    font-family: "Archivo Narrow", Arial, sans-serif;
    font-weight: 700;
    font-size: 34px;
    line-height: 1.18;
    color: var(--brand-yellow);
    white-space: nowrap;
  }
</style>
</head>
<body>
  <main class="cover">
    <div class="cover-photo" role="img" aria-label="Cover photograph: a marina at sunset with rows of moored sailboats and tall masts under an orange sky, reflected in calm teal water"></div>

    <header class="masthead">
      <p class="tagline">We Go Where The Wind Blows</p>
      <h1 class="brand-name">Brinehaven 52</h1>
      <p class="issue-line">VOLUME 01 | DECEMBER 2019</p>
    </header>

    <section class="cover-lines">
      <h2 class="lead-story">Shift Your<br>Mindset</h2>
      <ul class="teasers">
        <li>Season Champs Part 2</li>
        <li>Where'd Windsurfing Go?</li>
        <li>Rafael Oduya's New Coat of Paint</li>
      </ul>
    </section>
  </main>
</body>
</html>
```